Quellmark Exteriors Needs a New Website!

We are an exteriors company specializing in vinyl siding, Morten Calloway siding, aluminum soffit/fascia, trough. We do new construction work as well as renovations. We also build detached garages.
You can view our current website at www.quellmarkbuilders.ca
I want to completely overhaul the website.
Our services are different now as we no longer do new home construction as well as we do not do the snow clearing.
I want to focus on 2 things in particular on the website:

1/ Exterior renovations

2/ Detached Garage construction.

I have included our logo in the attached files to use as well.

Some features we would like:

1/ Be able to easily attach a video from Youtube/Vimeo to highlight a product or service
2/ Quick chat or contact button that we can talk to a potential client quickly
3/ Meet the Team page that is interesting and fresh
4/ Place for us to put in helpful exterior tips/suggestions for homeowners.

Content is not important, but looking for the best design that will attract people once they click on our page and want to renovate with us.

Target Market(s)

People looking for renovations on their home, people looking to build a detached garage.

Industry/Entity Type

Residential Construction

Coding

Coded - Design and coding required

Number of Pages Required

5+ page

Font styles to use
Sans Serif

Requirements
Must have
• Fresh and exciting home page.

Simple design. Don't want it over complicated or too much information to confuse the potential client.

Easy way to contact us.

Meet the team page that instills confidence
Nice to have
• Colour of website to go off our logo. Doesn't need to be an exact match, but something that goes well with our blue and grey.

```html
<!DOCTYPE html>
<html lang="en">
<head>
<meta charset="utf-8">
<title>Quellmark Exteriors</title>
<link rel="stylesheet" href="https://fonts.googleapis.com/css2?family=Montserrat:wght@400;500;600;700&family=Mulish:wght@400;600;700&display=swap">
<style>
:root{
  --blue:#0b6cbf;
  --blue-dark:#0865b3;
  --ink:#2a2a2a;
  --text:#555;
  --light:#f2f2f2;
  --footer:#616161;
  --footer-dark:#4d4d4d;
  --white:#fff;
}
*{box-sizing:border-box;margin:0;padding:0}
html,body{width:1200px;height:3676px;overflow:hidden}
body{position:relative;font-family:'Mulish',sans-serif;color:var(--text);background:var(--white)}
.abs{position:absolute}
.btn{position:absolute;display:flex;align-items:center;justify-content:center;background:var(--blue);color:var(--white);font-family:'Montserrat',sans-serif;font-weight:700;font-size:13px;letter-spacing:.6px;border-radius:3px;white-space:nowrap}
.heading{font-family:'Montserrat',sans-serif;font-weight:400;color:var(--ink);text-transform:uppercase}
.heading b{color:var(--blue);font-weight:700}
.rule{position:absolute;height:2px;width:64px;background:var(--blue)}

/* top bar */
.topbar{left:0;top:0;width:1200px;height:38px;background:var(--blue-dark);color:var(--white);font-size:14px}
.topbar .item{position:absolute;top:10px;display:flex;align-items:center;gap:8px}
.social{position:absolute;display:flex;gap:6px}
.social span{width:24px;height:24px;border-radius:50%;border:2px solid var(--white);background:#2e86d2}
.social.footer-social span{border-color:#ddd;background:var(--blue)}

/* header */
.header{left:0;top:38px;width:1200px;height:83px;background:var(--white)}
.brand{position:absolute;display:flex;align-items:center;gap:10px;font-family:'Montserrat',sans-serif;font-weight:700;color:var(--blue);white-space:nowrap}
.brand .mark{width:48px;height:48px;border-radius:50%;border:4px solid var(--blue)}
.nav{position:absolute;left:434px;top:34px;display:flex;gap:24px;font-family:'Montserrat',sans-serif;font-size:13px;color:#444;white-space:nowrap}
.nav .active{color:var(--blue);font-weight:700}

/* hero */
.hero{left:0;top:121px;width:1200px;height:526px;background:linear-gradient(180deg,#b3a7c9 0%,#8c86b4 30%,#4b5575 65%,#3b3d45 100%)}
.hero-title{position:absolute;left:0;top:288px;width:1200px;text-align:center;font-family:'Montserrat',sans-serif;font-weight:700;font-size:43px;line-height:51px;color:var(--white);text-shadow:0 2px 6px rgba(0,0,0,.45)}

/* about */
.about-photo{left:143px;top:735px;width:392px;height:378px;border:5px solid var(--white);box-shadow:0 0 0 1px #e3e3e3;background:linear-gradient(180deg,#9aa0a8 0%,#b8b5ae 50%,#6f7f52 100%)}
.play{position:absolute;left:164px;top:152px;width:64px;height:64px}
.about-title{left:578px;top:760px;font-size:29px;white-space:nowrap}
.about-title small{font-size:16px;color:#444}
.about-lead{left:578px;top:823px;width:481px;font-size:14px;line-height:24px;font-weight:700;color:var(--ink)}
.about-body{left:578px;top:876px;width:481px;font-size:12.5px;line-height:21.7px;text-align:justify;letter-spacing:.2px}

/* services */
.services{left:0;top:1203px;width:1200px;height:657px;background:var(--light)}
.section-title{position:absolute;left:0;width:1200px;text-align:center;font-size:29px}
.card{position:absolute;top:153px;width:444px;height:419px;background:var(--white);border-bottom:2px solid var(--blue)}
.card .photo{position:absolute;left:6px;top:4px;width:432px;height:231px}
.card h3{position:absolute;left:0;top:264px;width:100%;text-align:center;font-family:'Montserrat',sans-serif;font-weight:400;font-size:19.5px;color:var(--ink);text-transform:uppercase;letter-spacing:.4px;white-space:nowrap}
.card h3 b{font-weight:700}
.card p{position:absolute;left:0;top:297px;width:444px;text-align:center;font-size:12px;line-height:22px;white-space:nowrap}

/* gallery */
.tile{position:absolute}
.tile-caption{position:absolute;left:0;top:100px;width:100%;text-align:center;font-family:'Montserrat',sans-serif;font-weight:600;font-size:16.5px;line-height:22px;color:var(--white)}

/* cta */
.cta{left:0;top:2583px;width:1200px;height:317px;background:linear-gradient(180deg,#3c4654 0%,#2b333e 60%,#262b30 100%)}
.cta-sub{position:absolute;left:0;top:88px;width:1200px;text-align:center;font-size:18px;color:#e8e8e8}
.cta-title{position:absolute;left:0;top:118px;width:1200px;text-align:center;font-family:'Montserrat',sans-serif;font-weight:500;font-size:32px;color:var(--white)}

/* inquiry */
.footer{left:0;top:3305px;width:1200px;height:331px;background:var(--footer)}
.inquiry{left:275px;top:2982px;width:651px;height:400px;background:var(--light)}
.fold{position:absolute;left:0;bottom:0;width:74px;height:38px}
.field{position:absolute;background:var(--white);font-size:12.5px;color:#555;padding:10px 13px}

/* footer */
.f-head{position:absolute;top:3436px;font-family:'Montserrat',sans-serif;font-size:12px;color:var(--white);letter-spacing:.4px}
.f-head b{font-weight:700}
.f-links{position:absolute;left:143px;top:3463px;list-style:none;font-size:12.5px;color:#eee}
.f-links li{height:25.3px}
.f-links li::before{content:"»";margin-right:10px;font-size:11px}
.f-contact{position:absolute;left:320px;top:3463px;font-size:12.5px;line-height:18px;color:#eee}
.f-contact .row{display:flex;gap:8px;margin-bottom:7px}
.f-contact svg{flex:none;margin-top:2px}
.map{left:584px;top:3464px;width:210px;height:126px;border:3px solid #e6e6e6;background:linear-gradient(135deg,#eeeeee,#dcdcdc)}
.copyright{left:0;top:3636px;width:1200px;height:40px;background:var(--footer-dark);text-align:center;font-size:11.5px;line-height:40px;color:#eee}
.copyright b{font-weight:700}
</style>
</head>
<body>

<div class="abs topbar">
  <div class="item" style="left:141px">
    <svg width="14" height="14" viewBox="0 0 24 24"><path fill="#fff" d="M6.6 10.8a15.1 15.1 0 0 0 6.6 6.6l2.2-2.2a1 1 0 0 1 1-.25 11.4 11.4 0 0 0 3.6.6 1 1 0 0 1 1 1V20a1 1 0 0 1-1 1A17 17 0 0 1 3 4a1 1 0 0 1 1-1h3.5a1 1 0 0 1 1 1c0 1.25.2 2.45.6 3.6a1 1 0 0 1-.25 1z"/></svg>
    <span>780-555-0148</span>
  </div>
  <div class="item" style="left:281px">
    <svg width="16" height="12" viewBox="0 0 16 12"><rect x="0.5" y="0.5" width="15" height="11" fill="none" stroke="#fff"/><path d="M1 1l7 6 7-6" fill="none" stroke="#fff"/></svg>
    <span>info@quellmarkbuilders.ca</span>
  </div>
  <div class="social" style="left:941px;top:7px"><span></span><span></span><span></span><span></span></div>
</div>

<header class="abs header">
  <div class="brand" style="left:141px;top:15px;font-size:28px"><span class="mark"></span>QUELLMARK</div>
  <nav class="nav">
    <span class="active">HOME</span><span>ABOUT</span><span>SERVICES</span><span>MEET THE TEAM</span><span>CONTACT</span>
  </nav>
  <div class="btn" style="left:889px;top:22px;width:170px;height:40px">REQUEST A QUOTE</div>
</header>

<section class="abs hero" role="img" aria-label="Two-storey house with lit windows at dusk">
  <h1 class="hero-title">EXPERIENCE THE<br>QUELLMARK DIFFERENCE</h1>
  <div class="btn" style="left:504px;top:409px;width:191px;height:39px">GET STARTED TODAY</div>
</section>

<div class="abs about-photo" role="img" aria-label="Video thumbnail of a finished two-storey home exterior">
  <svg class="play" viewBox="0 0 64 64"><circle cx="32" cy="32" r="30" fill="none" stroke="#fff" stroke-width="2.5"/><path d="M25 20l20 12-20 12z" fill="none" stroke="#fff" stroke-width="2.5" stroke-linejoin="round"/></svg>
</div>
<h2 class="abs heading about-title">About <b>Quellmark</b> <small>Exteriors</small></h2>
<div class="rule" style="left:578px;top:804px"></div>
<p class="abs about-lead">Lorem ipsum dolor sit amet, consectetuer adipiscing elit, sed diam nonummy nibh euismod tincidunt ut laoreet dolore.</p>
<p class="abs about-body">Lorem ipsum dolor sit amet, consectetuer adipiscing elit, sed diam nonummy nibh euismod tincidunt ut laoreet dolore magna aliquam erat volutpat. Ut wisi enim ad minim veniam, quis nostrud exerci tation ullamcorper suscipit lobortis nisl ut aliquip ex ea commodo consequat. Duis autem vel eum iriure dolor in hendrerit in vulputate velit esse molestie consequat, vel illum dolore eu feugiat nulla facilisis at vero eros et accumsan et iusto odio dignissim qui blandit praesent luptatum zzril delenit augue duis dolore te facilisi.</p>
<div class="btn" style="left:578px;top:1046px;width:128px;height:39px">READ MORE</div>

<section class="abs services">
  <h2 class="heading section-title" style="top:75px">Our <b>Services</b></h2>
  <div class="rule" style="left:568px;top:121px"></div>
  <article class="card" style="left:141px">
    <div class="photo" role="img" aria-label="Renovated home exterior with grey siding and white trim" style="background:linear-gradient(180deg,#9fb0a0 0%,#68707a 55%,#7d8a4e 100%)"></div>
    <h3>Exterior <b>Renovations</b></h3>
    <p>Quellmark's goal is to be the best home and building exterior<br>renovations company in the Edmonton area...</p>
    <div class="btn" style="left:157px;top:356px;width:129px;height:38px">READ MORE</div>
  </article>
  <article class="card" style="left:615px">
    <div class="photo" role="img" aria-label="Timber-framed detached garage under construction" style="background:linear-gradient(180deg,#8fb3c9 0%,#b98b61 50%,#6e8a4e 100%)"></div>
    <h3>Detached Garage <b>Construction</b></h3>
    <p>Lorem ipsum dolor sit amet, consectetuer adipiscing elit, sed diam<br>nonummy nibh euismod tincidunt ut laoreet dolore magna...</p>
    <div class="btn" style="left:157px;top:356px;width:129px;height:38px">READ MORE</div>
  </article>
</section>

<h2 class="heading section-title abs" style="top:1937px">Work <b>Gallery</b></h2>
<div class="rule" style="left:568px;top:1983px"></div>
<div class="tile" role="img" aria-label="House exterior under construction" style="left:141px;top:2019px;width:297px;height:183px;background:linear-gradient(180deg,#b7b7b7,#6b5a4a)"></div>
<div class="tile" role="img" aria-label="Dark-sided new home with stone accents" style="left:141px;top:2213px;width:297px;height:220px;background:linear-gradient(180deg,#c9c9c9,#3f4550 70%,#8a8a80)"></div>
<div class="tile" role="img" aria-label="Modern dark home exterior at dusk" style="left:452px;top:2019px;width:296px;height:243px;background:linear-gradient(180deg,#4a4d52,#2a2c30)">
  <div class="tile-caption">Unrivalled Quality and<br>Attention to Detail</div>
</div>
<div class="tile" role="img" aria-label="Lit contemporary home with patio at evening" style="left:452px;top:2273px;width:296px;height:160px;background:linear-gradient(180deg,#6a6f55,#8b5a2e 60%,#3a3025)"></div>
<div class="tile" role="img" aria-label="Wooden interior staircase framing" style="left:762px;top:2019px;width:297px;height:162px;background:linear-gradient(135deg,#a06a40,#d9b48c 50%,#7a4c2c)"></div>
<div class="tile" role="img" aria-label="Finished kitchen with grey cabinets and island" style="left:762px;top:2192px;width:297px;height:241px;background:linear-gradient(180deg,#e8e8e6,#9a948c 60%,#cfcac2)"></div>
<div class="btn" style="left:543px;top:2460px;width:114px;height:37px">VIEW ALL</div>

<section class="abs cta" role="img" aria-label="House framing with scaffolding, darkened background">
  <p class="cta-sub">Honest And Reliable Construction Service In Edmonton And Area.</p>
  <h2 class="cta-title">We Take Pride In Each And Every Project</h2>
  <div class="btn" style="left:508px;top:185px;width:184px;height:38px">REQUEST A QUOTE</div>
</section>

<div class="abs footer"></div>

<section class="abs inquiry">
  <h2 class="heading section-title" style="left:0;width:651px;top:50px;position:absolute">Quick <b>Inquiry</b></h2>
  <div class="rule" style="left:293px;top:93px"></div>
  <div class="field" style="left:86px;top:123px;width:231px;height:34px">Name</div>
  <div class="field" style="left:333px;top:123px;width:232px;height:34px">Email</div>
  <div class="field" style="left:86px;top:167px;width:231px;height:34px">Phone</div>
  <div class="field" style="left:333px;top:167px;width:232px;height:34px">Service</div>
  <div class="field" style="left:86px;top:211px;width:479px;height:72px">Message</div>
  <div class="btn" style="left:257px;top:304px;width:136px;height:37px">SUBMIT NOW</div>
  <svg class="fold" viewBox="0 0 74 38"><path d="M0 0 L38 38 L0 38 Z" fill="#0b6cbf"/><path d="M38 0 L74 38 L38 38 Z" fill="#d8d8d8"/></svg>
</section>

<div class="f-head" style="left:143px">QUICK <b>LINKS</b></div>
<ul class="f-links"><li>Home</li><li>About</li><li>Services</li><li>Meet The Team</li><li>Contact</li></ul>

<div class="f-head" style="left:320px">CONTACT <b>DETAILS</b></div>
<div class="f-contact">
  <div class="row"><svg width="11" height="14" viewBox="0 0 12 16"><path d="M6 0a6 6 0 0 0-6 6c0 4.5 6 10 6 10s6-5.5 6-10a6 6 0 0 0-6-6zm0 8.5A2.5 2.5 0 1 1 6 3.5a2.5 2.5 0 0 1 0 5z" fill="#fff"/></svg><div>QUELLMARK EXTERIORS<br>118-40217 RR 204<br>Ashgrove, AB T0B 2K4</div></div>
  <div class="row"><svg width="12" height="12" viewBox="0 0 24 24"><path fill="#fff" d="M6.6 10.8a15.1 15.1 0 0 0 6.6 6.6l2.2-2.2a1 1 0 0 1 1-.25 11.4 11.4 0 0 0 3.6.6 1 1 0 0 1 1 1V20a1 1 0 0 1-1 1A17 17 0 0 1 3 4a1 1 0 0 1 1-1h3.5a1 1 0 0 1 1 1c0 1.25.2 2.45.6 3.6a1 1 0 0 1-.25 1z"/></svg><div>780-555-0148</div></div>
  <div class="row"><svg width="13" height="10" viewBox="0 0 16 12"><rect x="0.5" y="0.5" width="15" height="11" fill="none" stroke="#fff"/><path d="M1 1l7 6 7-6" fill="none" stroke="#fff"/></svg><div>info@quellmarkbuilders.ca</div></div>
</div>

<div class="f-head" style="left:584px">LOCATION <b>MAP</b></div>
<div class="abs map" role="img" aria-label="Location map of the company office"></div>

<div class="brand" style="left:860px;top:3482px;font-size:25px;color:#eee"><span class="mark" style="border-color:#eee;width:44px;height:44px"></span>QUELLMARK</div>
<div class="social footer-social" style="left:909px;top:3556px"><span></span><span></span><span></span><span></span></div>

<div class="abs copyright">Copyright © 2020 <b>QUELLMARK EXTERIORS</b>. All Rights Reserved.</div>

</body>
</html>
```